Brazilian food stall looking for a make over

We need a new Design for the front of our stall that would look authentic, colourful and practical as we have to transport, set up and put down in few hours.
We are based in Brisbane and our business are call The Ember Stand.
We sell Brazilian traditional BBQ and vegetarians options at markets, festivals and privet functions. We are new to this business and at the moment we are using our own design as presented on the image below.
We would like to see designs that would be eye catching with high contrast for easy recognition of the product with a menu with images of the product.

Requirements
Must have
• A connection with the product that is Brazilian bbq

```html
<!DOCTYPE html>
<html lang="en">
<head>
<meta charset="utf-8">
<title>The Ember Stand</title>
<link rel="stylesheet" href="https://fonts.googleapis.com/css2?family=Caprasimo&display=swap">
<style>
  :root {
    --flag-green: #169c4a;
    --flag-yellow: #fbde0a;
    --ember-brown: #b4541f;
    --grill-char: #2e1a12;
    --grill-smoke: #5a3a2c;
    --grill-flame: #d0702e;
    --meat-rare: #b85a4e;
    --meat-crust: #7a3420;
  }
  html, body {
    margin: 0;
    padding: 0;
    overflow: hidden;
    background: #ffffff;
  }
  .stall-banner {
    position: relative;
    width: 1200px;
    height: 280px;
    overflow: hidden;
    background: var(--flag-green);
  }
  .banner-shapes {
    position: absolute;
    inset: 0;
    display: block;
  }
  .diamond { fill: var(--flag-yellow); }
  .title-band { fill: var(--flag-yellow); }
  .brand-name {
    position: absolute;
    left: 0;
    right: 0;
    top: 98px;
    height: 82px;
    margin: 0;
    display: flex;
    align-items: center;
    justify-content: center;
    font-family: "Caprasimo", "Cooper Black", serif;
    font-weight: 400;
    font-size: 76px;
    line-height: 1;
    letter-spacing: 1px;
    white-space: nowrap;
    color: var(--ember-brown);
  }
</style>
</head>
<body>
  <div class="stall-banner">
    <svg class="banner-shapes" width="1200" height="280" viewBox="0 0 1200 280" xmlns="http://www.w3.org/2000/svg">
      <defs>
        <linearGradient id="grill-tones" x1="0" y1="0" x2="0" y2="1">
          <stop offset="0%" stop-color="var(--grill-smoke)"/>
          <stop offset="18%" stop-color="var(--grill-flame)"/>
          <stop offset="34%" stop-color="var(--meat-crust)"/>
          <stop offset="62%" stop-color="var(--meat-rare)"/>
          <stop offset="82%" stop-color="var(--meat-crust)"/>
          <stop offset="100%" stop-color="var(--grill-char)"/>
        </linearGradient>
      </defs>
      <polygon class="diamond" points="138,140 276,0 924,0 1062,140 924,280 276,280"/>
      <circle class="grill-photo" cx="600" cy="170" r="258" fill="url(#grill-tones)"
              role="img" aria-label="Photo of Brazilian churrasco: picanha beef and sausages roasting on skewers over glowing coals, a rare sliced cut in front"/>
      <rect class="title-band" x="246" y="98" width="708" height="82"/>
    </svg>
    <h1 class="brand-name">The Ember Stand</h1>
  </div>
</body>
</html>
```